Tamsyndale - Elevating shareholder relations with a seamless SaaS communication platform

We need a landing page / web page for a new company based in Stockholm called "Tamsyndale". Our platform helps private companies communicate & connect with their shareholders and provides a cost efficient way of raising funds. We would like to see designs that use the color blue.

```html
<!DOCTYPE html>
<html lang="en">
<head>
<meta charset="utf-8">
<title>Tamsyndale - Elevating shareholder relations with a seamless SaaS communication platform</title>
<link rel="stylesheet" href="https://fonts.googleapis.com/css2?family=Montserrat:wght@400;500;600;700;800&family=Roboto:wght@400;500&display=swap">
<style>
:root{
  --navy:#1a5996;
  --blue:#2266a8;
  --sky:#6c9fd0;
  --pale:#dfe9f4;
  --ink:#1d1d1d;
  --grey:#6e6e6e;
  --line:#c9c9c9;
  --white:#ffffff;
}
*{margin:0;padding:0;box-sizing:border-box}
html,body{width:1200px;height:3539px;overflow:hidden;background:var(--white)}
body{position:relative;font-family:'Montserrat',sans-serif;color:var(--ink)}
.abs{position:absolute}

/* header */
.topbar{left:468px;top:0;width:732px;height:47px;background:var(--navy);clip-path:polygon(0 0,100% 0,100% 100%,18px 100%);color:var(--white);font-size:15px;display:flex;align-items:center}
.topbar .item{display:flex;align-items:center;gap:12px;margin-left:40px}
.dots{margin-left:auto;margin-right:60px;display:flex;gap:12px}
.dot{width:31px;height:31px;border-radius:50%;background:var(--white)}
.brand{left:70px;top:40px;width:200px;text-align:center;font-weight:600;font-size:17px;letter-spacing:3px;color:var(--navy)}
.brand .mark{display:block;margin:0 auto 10px;width:52px;height:52px;background:var(--navy)}
.nav{left:322px;top:80px;display:flex;gap:41px;font-size:17px;font-weight:500}
.login{left:931px;top:67px;width:173px;height:46px;border-radius:23px;background:var(--blue);color:var(--white);font-size:21px;font-weight:500;display:flex;align-items:center;justify-content:center}

/* hero */
.hero{left:0;top:129px;width:1200px;height:648px;background:linear-gradient(100deg,#c9c4bd 0%,#ddd9d3 35%,#a8b8c8 65%,#e9e6e1 100%)}
.hero-band{left:0;top:700px;width:1200px;height:80px}
.hero-panel{left:58px;top:238px;width:592px;height:353px;background:rgba(86,136,188,.78)}
.hero-title{left:93px;top:274px;width:550px;font-size:31.5px;line-height:51px;color:var(--white);font-weight:400;text-transform:uppercase;white-space:nowrap}
.hero-title b{font-weight:800}
.btn{display:flex;align-items:center;gap:14px;border-radius:28px;background:var(--blue);color:var(--white);font-weight:500}
.btn .disc{width:30px;height:30px;border-radius:50%;background:var(--white)}
.hero-btn{left:91px;top:498px;width:203px;height:55px;padding-left:13px;font-size:18px}

/* about */
.about-hex{left:93px;top:828px;width:408px;height:470px}
.about-kicker{left:578px;top:857px;font-size:29px;font-weight:400;letter-spacing:1px}
.about-name{left:578px;top:893px;font-size:39px;font-weight:800;color:var(--navy);letter-spacing:1px}
.about-name span{color:var(--sky)}
.about-copy{left:578px;top:957px;width:476px;font-size:14.6px;line-height:25.7px;color:var(--grey);text-align:justify}
.about-btn{left:579px;top:1160px;width:172px;height:47px;padding-left:10px;font-size:15px;background:var(--navy)}
.side-word{left:1108px;top:850px;writing-mode:vertical-rl;font-size:34px;font-weight:800;color:var(--pale);letter-spacing:2px}
.side-line{left:1122px;top:775px;width:2px;height:65px;background:var(--sky)}

/* services */
.services{left:0;top:1375px;width:1200px;height:610px}
.svc-title{left:0;top:1430px;width:1200px;text-align:center;color:var(--white);font-size:29px;font-weight:700;letter-spacing:1px}
.card{top:1503px;width:244px;height:371px;background:var(--white);text-align:center}
.card .photo{height:198px}
.card h3{margin-top:28px;font-size:21px;font-weight:700;letter-spacing:.5px}
.card p{margin:12px auto 0;width:205px;font-size:14.5px;line-height:20.5px;color:#555}
.play{width:48px;height:54px;top:1848px}

/* why */
.why-title{left:0;top:2066px;width:1200px;text-align:center;color:var(--navy);font-size:24px;font-weight:700}
.why{top:2130px;width:330px;text-align:center}
.why svg{display:block;margin:0 auto}
.why h3{margin-top:18px;color:var(--navy);font-size:25px;font-weight:600;letter-spacing:.3px}
.why p{margin:30px auto 0;width:285px;font-family:'Roboto',sans-serif;font-size:15px;line-height:26px;color:#555}

/* contact */
.contact{left:0;top:2582px;width:1200px;height:484px;background:linear-gradient(180deg,#f1f1f1,#e6e6e6)}
.contact-title{left:0;top:2665px;width:1200px;text-align:center;color:var(--navy);font-size:25px;font-weight:700}
.field{height:48px;border:1.5px solid var(--line);border-radius:14px;background:var(--white);font-size:11px;color:#444;padding:18px 0 0 16px}
.submit{left:514px;top:2981px;width:171px;height:48px;border-radius:24px;background:var(--navy);color:var(--white);font-size:18px;font-weight:500;display:flex;align-items:center;justify-content:center}

/* footer */
.footer{left:0;top:3055px;width:1200px;height:484px;background:var(--navy)}
.foot-brand{left:90px;top:3190px;width:240px;text-align:center;color:var(--white);font-weight:600;font-size:28px;letter-spacing:4px}
.foot-brand .mark{display:block;margin:0 auto 22px;width:100px;height:100px;border:3px solid var(--white)}
.foot-social{left:92px;top:3390px;display:flex;gap:22px}
.foot-social span{width:26px;height:26px;border-radius:50%;border:2px solid var(--white)}
.col{top:3187px;color:var(--white)}
.col h4{font-size:21px;font-weight:500;margin-bottom:22px;letter-spacing:.5px}
.col li{list-style:none;font-family:'Roboto',sans-serif;font-weight:500;font-size:15.5px;height:32px;display:flex;align-items:center;gap:13px}
.col li::before{content:"";border-left:6px solid var(--white);border-top:5px solid transparent;border-bottom:5px solid transparent}
.info{display:flex;gap:14px;font-family:'Roboto',sans-serif;font-size:15.5px;line-height:25px;margin-bottom:14px}
.foot-rule{left:98px;top:3455px;width:1004px;height:1px;background:rgba(255,255,255,.5)}
.copy{left:0;top:3484px;width:1200px;text-align:center;color:var(--white);font-family:'Roboto',sans-serif;font-size:15.5px}
</style>
</head>
<body>

<header>
  <div class="abs topbar">
    <div class="item">
      <svg width="14" height="14" viewBox="0 0 24 24"><path fill="#fff" d="M6.6 10.8a15 15 0 0 0 6.6 6.6l2.2-2.2a1 1 0 0 1 1-.25 11.4 11.4 0 0 0 3.6.57 1 1 0 0 1 1 1V20a1 1 0 0 1-1 1A17 17 0 0 1 3 4a1 1 0 0 1 1-1h3.5a1 1 0 0 1 1 1c0 1.250.2 2.45.57 3.57a1 1 0 0 1-.25 1z"/></svg>
      <span>+46 8 555 0142</span>
    </div>
    <div class="item">
      <svg width="16" height="12" viewBox="0 0 16 12"><rect width="16" height="12" rx="1" fill="#fff"/><path d="M0 1l8 6 8-6" stroke="#1a5996" stroke-width="1.5" fill="none"/></svg>
      <span>hello@tamsyndale.example</span>
    </div>
    <div class="dots"><span class="dot"></span><span class="dot"></span><span class="dot"></span></div>
  </div>
  <div class="abs brand"><span class="mark"></span>TAMSYNDALE</div>
  <nav class="abs nav"><span>HOME</span><span>ABOUT</span><span>SERVICES</span><span>BLOG</span><span>NEWS</span><span>CONTACT</span></nav>
  <div class="abs login">LOGIN</div>
</header>

<section>
  <div class="abs hero" role="img" aria-label="Photo of a smiling businessman working on a laptop in a bright office"></div>
  <svg class="abs hero-band" viewBox="0 0 1200 80" preserveAspectRatio="none">
    <polygon points="0,77 1200,28 1200,80 0,80" fill="#fff"/>
    <polygon points="560,57 1200,2 1200,62" fill="#6c9fd0"/>
  </svg>
  <div class="abs hero-panel"></div>
  <h1 class="abs hero-title">Elevating <b>shareholder</b><br>relations with a seamless<br>SaaS <b>communication</b><br>platform</h1>
  <div class="abs btn hero-btn"><span class="disc"></span>GET STARTED</div>
</section>

<section>
  <svg class="abs about-hex" viewBox="0 0 408 470">
    <defs>
      <clipPath id="inner"><polygon points="204,38 372,135 372,335 204,432 36,335 36,135"/></clipPath>
      <linearGradient id="city" x1="0" y1="0" x2="0" y2="1"><stop offset="0" stop-color="#3d6f9c"/><stop offset=".55" stop-color="#8fb3cf"/><stop offset="1" stop-color="#1f3f66"/></linearGradient>
    </defs>
    <polygon points="204,0 408,118 408,352 204,470 0,352 0,118" fill="#1a5996"/>
    <g clip-path="url(#inner)" role="img" aria-label="Photo of a businessman overlooking a city skyline at dusk">
      <rect width="408" height="470" fill="url(#city)"/>
    </g>
  </svg>
  <div class="abs side-line"></div>
  <div class="abs side-word">TAMSYNDALE</div>
  <h2 class="abs about-kicker">ABOUT US</h2>
  <div class="abs about-name">TAMSYN<span>DALE</span></div>
  <p class="abs about-copy">Lorem ipsum dolor sit amet, consectetur adipiscing elit, sed do eiusmod tempor incididunt ut labore et dolore magna aliqua. Ut enim ad minim veniam, quis nostrud exercitation ullamco laboris nisi ut aliquip ex ea commodo consequat. Duis aute irure dolor in reprehenderit in voluptate velit esse cillum dolore eu fugiat nulla pariatur. Excepteur sint occaecat cupidatat non proident, sunt in culpa qui officia deserunt mollit anim id est laborum."</p>
  <div class="abs btn about-btn"><span class="disc"></span>READ MORE</div>
</section>

<section>
  <svg class="abs services" viewBox="0 0 1200 610" preserveAspectRatio="none">
    <defs><linearGradient id="svcbg" x1="0" y1="0" x2="0" y2="1"><stop offset="0" stop-color="#1d5a95"/><stop offset=".6" stop-color="#2a6aa6"/><stop offset="1" stop-color="#1a5590"/></linearGradient></defs>
    <polygon points="0,15 1200,0 1200,595 0,610" fill="url(#svcbg)"/>
    <polygon points="600,12 1200,0 1200,30" fill="#6c9fd0"/>
    <polygon points="0,560 1200,590 0,610" fill="#6c9fd0"/>
  </svg>
  <h2 class="abs svc-title">OUR SERVICE</h2>

  <div class="abs card" style="left:94px"><div class="photo" role="img" aria-label="Photo of a businessman on the phone at a laptop" style="background:linear-gradient(135deg,#d9d2c7,#8a8276)"></div><h3>LOREM IPSUM</h3><p>Duis aute irure dolor in reprehenderit in voluptate velit esse cillum dolore eu fugiat nulla pariatur.</p></div>
  <div class="abs card" style="left:349px"><div class="photo" role="img" aria-label="Photo of a team meeting around a table" style="background:linear-gradient(135deg,#e6e3de,#5f6f84)"></div><h3>LOREM IPSUM</h3><p>Duis aute irure dolor in reprehenderit in voluptate velit esse cillum dolore eu fugiat nulla pariatur.</p></div>
  <div class="abs card" style="left:605px"><div class="photo" role="img" aria-label="Photo of business people in a glass office" style="background:linear-gradient(135deg,#9fc0de,#e7c3b8)"></div><h3>LOREM IPSUM</h3><p>Duis aute irure dolor in reprehenderit in voluptate velit esse cillum dolore eu fugiat nulla pariatur.</p></div>
  <div class="abs card" style="left:859px"><div class="photo" role="img" aria-label="Photo of a hand touching a glowing financial chart" style="background:linear-gradient(135deg,#123f6e,#2a86b5)"></div><h3>LOREM IPSUM</h3><p>Duis aute irure dolor in reprehenderit in voluptate velit esse cillum dolore eu fugiat nulla pariatur.</p></div>

  <svg class="abs play" style="left:193px" viewBox="0 0 48 54"><polygon points="24,0 48,13.5 48,40.5 24,54 0,40.5 0,13.5" fill="#6c9fd0"/><polygon points="19,17 33,27 19,37" fill="#fff"/></svg>
  <svg class="abs play" style="left:447px" viewBox="0 0 48 54"><polygon points="24,0 48,13.5 48,40.5 24,54 0,40.5 0,13.5" fill="#6c9fd0"/><polygon points="19,17 33,27 19,37" fill="#fff"/></svg>
  <svg class="abs play" style="left:703px" viewBox="0 0 48 54"><polygon points="24,0 48,13.5 48,40.5 24,54 0,40.5 0,13.5" fill="#6c9fd0"/><polygon points="19,17 33,27 19,37" fill="#fff"/></svg>
  <svg class="abs play" style="left:957px" viewBox="0 0 48 54"><polygon points="24,0 48,13.5 48,40.5 24,54 0,40.5 0,13.5" fill="#6c9fd0"/><polygon points="19,17 33,27 19,37" fill="#fff"/></svg>
</section>

<section>
  <h2 class="abs why-title">WHY CHOOSE US</h2>
  <div class="abs why" style="left:70px">
    <svg width="180" height="180" viewBox="0 0 180 180"><circle cx="90" cy="90" r="87" fill="none" stroke="#1a5996" stroke-width="2" stroke-dasharray="6 5"/><circle cx="90" cy="90" r="69" fill="#6c9fd0"/><circle cx="84" cy="84" r="22" fill="none" stroke="#fff" stroke-width="4"/><line x1="100" y1="100" x2="116" y2="116" stroke="#fff" stroke-width="6" stroke-linecap="round"/><polyline points="70,90 80,80 88,86 98,74" fill="none" stroke="#fff" stroke-width="3"/></svg>
    <h3>DUIS AUTE IRURE</h3>
    <p>Lorem ipsum dolor sit amet, consectetur adipiscing elit, sed do eiusmod tempor incididunt ut labore et dolore magna aliqua Ut enim ad minim</p>
  </div>
  <div class="abs why" style="left:432px">
    <svg width="180" height="180" viewBox="0 0 180 180"><circle cx="90" cy="90" r="87" fill="none" stroke="#1a5996" stroke-width="2" stroke-dasharray="6 5"/><circle cx="90" cy="90" r="69" fill="#6c9fd0"/><polyline points="58,92 76,76 90,84 116,60" fill="none" stroke="#fff" stroke-width="4"/><polygon points="108,58 120,56 118,68" fill="#fff"/><circle cx="70" cy="108" r="9" fill="none" stroke="#fff" stroke-width="3"/><circle cx="92" cy="104" r="9" fill="none" stroke="#fff" stroke-width="3"/><circle cx="114" cy="98" r="9" fill="none" stroke="#fff" stroke-width="3"/><rect x="84" y="114" width="16" height="10" fill="#fff"/><rect x="106" y="110" width="16" height="14" fill="#fff"/></svg>
    <h3>DUIS AUTE IRURE</h3>
    <p>Lorem ipsum dolor sit amet, consectetur adipiscing elit, sed do eiusmod tempor incididunt ut labore et dolore magna aliqua Ut enim ad minim</p>
  </div>
  <div class="abs why" style="left:793px">
    <svg width="180" height="180" viewBox="0 0 180 180"><circle cx="90" cy="90" r="87" fill="none" stroke="#1a5996" stroke-width="2" stroke-dasharray="6 5"/><circle cx="90" cy="90" r="69" fill="#6c9fd0"/><polyline points="62,56 62,118 124,118" fill="none" stroke="#fff" stroke-width="3"/><polyline points="68,80 82,100 96,86 110,104 122,88" fill="none" stroke="#fff" stroke-width="3"/><line x1="70" y1="118" x2="70" y2="124" stroke="#fff" stroke-width="3"/><line x1="86" y1="118" x2="86" y2="124" stroke="#fff" stroke-width="3"/><line x1="102" y1="118" x2="102" y2="124" stroke="#fff" stroke-width="3"/><line x1="118" y1="118" x2="118" y2="124" stroke="#fff" stroke-width="3"/></svg>
    <h3>DUIS AUTE IRURE</h3>
    <p>Lorem ipsum dolor sit amet, consectetur adipiscing elit, sed do eiusmod tempor incididunt ut labore et dolore magna aliqua Ut enim ad minim</p>
  </div>
</section>

<section>
  <div class="abs contact"></div>
  <h2 class="abs contact-title">CONTACT US</h2>
  <div class="abs field" style="left:195px;top:2725px;width:398px">Fast Name</div>
  <div class="abs field" style="left:606px;top:2725px;width:399px">Last Name</div>
  <div class="abs field" style="left:195px;top:2788px;width:398px">Email</div>
  <div class="abs field" style="left:606px;top:2788px;width:399px">Phone Number</div>
  <div class="abs field" style="left:198px;top:2860px;width:803px;height:90px;padding-top:14px">Company</div>
  <div class="abs submit">SUBMIT</div>
</section>

<footer>
  <svg class="abs footer" viewBox="0 0 1200 484" preserveAspectRatio="none">
    <polygon points="0,60 1200,0 1200,484 0,484" fill="#1a5996"/>
    <polygon points="0,0 700,40 0,60" fill="#6c9fd0"/>
  </svg>
  <div class="abs foot-brand"><span class="mark"></span>TAMSYNDALE</div>
  <div class="abs foot-social"><span></span><span></span><span></span><span></span></div>
  <div class="abs col" style="left:424px"><h4>OUR MENU</h4><ul><li>Home</li><li>About</li><li>Services</li><li>Blog</li><li>News</li><li>Contact</li></ul></div>
  <div class="abs col" style="left:637px"><h4>HELP LINK</h4><ul><li>Terms&amp;condtions</li><li>Privacy Policy</li><li>About Us</li><li>Support</li></ul></div>
  <div class="abs col" style="left:876px;width:240px"><h4>CONTACT US</h4>
    <div class="info"><svg width="12" height="18" viewBox="0 0 12 18"><path d="M6 0a6 6 0 0 1 6 6c0 4.5-6 12-6 12S0 10.5 0 6a6 6 0 0 1 6-6z" fill="#fff"/><circle cx="6" cy="6" r="2.2" fill="#1a5996"/></svg><span>2712 Lorem ipsum dolor sit amet, consectetur</span></div>
    <div class="info"><svg width="14" height="14" viewBox="0 0 24 24"><path fill="#fff" d="M6.6 10.8a15 15 0 0 0 6.6 6.6l2.2-2.2a1 1 0 0 1 1-.25 11.4 11.4 0 0 0 3.6.57 1 1 0 0 1 1 1V20a1 1 0 0 1-1 1A17 17 0 0 1 3 4a1 1 0 0 1 1-1h3.5a1 1 0 0 1 1 1c0 1.25.2 2.45.57 3.57a1 1 0 0 1-.25 1z"/></svg><span>+46 8 555 0142</span></div>
    <div class="info" style="margin-top:12px"><svg width="16" height="12" viewBox="0 0 16 12" style="margin-top:6px"><rect width="16" height="12" rx="1" fill="#fff"/><path d="M0 1l8 6 8-6" stroke="#1a5996" stroke-width="1.5" fill="none"/></svg><span>hello@tamsyndale.example</span></div>
  </div>
  <div class="abs foot-rule"></div>
  <div class="abs copy">© copyrights 2022 © tamsyndale|&nbsp; All Rights Reserved</div>
</footer>

</body>
</html>
```